LORM Business Card Design Project

Company Name: LORM (Bright Harbor Computing Solutions) PGH.
Office Address: Office No 718, Saffron Crest Tower, Palmwood Garden Heights, Dubai, U.A.E
Company line of business:
1) Currently we have a POS solution for retail outlets like duty free shops, supermarkets, department stores etc... The solution is deployed in Coastline Travel Retail on 350 POS and in Sandgate Airport Retail on 100 POS. So our main line of business is the deployment of this solution in retail outlets locally or regionally. We have already deployed the solution in India and Australia.
2) Integration of other third party POS systems with an online credit authorization netwotk in the UAE. This will enable POS applications to connect directly to the acquiring banks without needing an EFT terminal like Paxtrel or Movarski. The credit card payment is completed at the POS.
3) Other solutions that are targeting retail outlets like mobile POS, queue busting solutions, stock taking solutions using hand held devices, transaction capture systems, etc...
4) Other IT services like support of call center solutions from Northwind Callworks and development of new solutions as per customer requirements.
We need a business card design for the company. We don't have any specific requirements and will eave up to the designers to come up with creative designs. At the moment we still don't have a letter head design and the only thing that we have is the company logo that we will upload shortly.
Updates
Dear All,
I just uploaded the logo source files. I am sorry for the delay.
Regards
Samir Odwani
I would like the business cards to have the following details:
Company Tel No
Company Fax No
Company Website Address
Employee Name
Employee Title
Employee Mobile Number
Employee Email Address

```html
<!DOCTYPE html>
<html lang="en">
<head>
<meta charset="utf-8">
<title>LORM Business Cards</title>
<link rel="stylesheet" href="https://fonts.googleapis.com/css2?family=Questrial&display=swap">
<style>
  :root {
    --backdrop: #ececec;
    --card: #e9e9ea;
    --ink: #3a3a3c;
    --ink-soft: #4a4a4c;
    --blue: #1aa0e0;
    --red: #e8282c;
    --band-green: #9ccb3b;
    --band-yellow: #d8e021;
    --band-blue: #1190d2;
  }
  * { box-sizing: border-box; margin: 0; padding: 0; }
  html, body {
    width: 1200px; height: 1069px; overflow: hidden;
    background: var(--backdrop);
    font-family: "Questrial", "Century Gothic", sans-serif;
    color: var(--ink);
  }
  .sheet { position: relative; width: 1200px; height: 1069px; }
  .card {
    position: absolute; width: 454px; height: 250px;
    background: var(--card); border-radius: 4px 14px 14px 4px; overflow: hidden;
  }
  .card--front-a { left: 84px; top: 256px; }
  .card--back-a  { left: 662px; top: 264px; }
  .card--front-b { left: 84px; top: 712px; }
  .card--back-b  { left: 662px; top: 718px; }

  .front-mark {
    position: absolute; left: 0; right: 0; top: 98px;
    display: flex; justify-content: center; align-items: center; gap: 14px;
  }
  .mark-dot { width: 34px; height: 34px; border-radius: 50%; background: var(--blue); }
  .mark-name { font-size: 48px; line-height: 1; letter-spacing: 2px; color: var(--ink); }

  .holder { position: absolute; left: 42px; top: 42px; }
  .holder-name { font-size: 24px; letter-spacing: -0.3px; color: var(--ink-soft); }
  .holder-title { font-size: 14px; margin-left: 96px; margin-top: 2px; }
  .holder-title--blue { color: var(--blue); }
  .holder-title--red { color: var(--red); margin-left: 98px; }

  .back-mark {
    position: absolute; right: 30px; top: 46px;
    display: flex; align-items: center; gap: 8px;
  }
  .back-mark .mark-dot { width: 20px; height: 20px; }
  .back-mark .mark-name { font-size: 28px; }

  .detail { position: absolute; font-size: 10.5px; line-height: 13.5px; color: var(--ink); white-space: nowrap; }
  .detail .indent { display: block; padding-left: 48px; }
  .address { left: 40px; top: 108px; }
  .personal { left: 37px; top: 148px; }
  .company-line { left: 0; right: 0; text-align: center; top: 212px; line-height: 16px; }
  .company-line .gap { display: inline-block; width: 18px; }
  .company-col { left: 292px; top: 150px; }

  .color-band {
    position: absolute; left: 0; right: 0; bottom: 0; height: 46px;
    background: linear-gradient(90deg, var(--band-green) 0%, var(--band-yellow) 55%, var(--band-blue) 75%, var(--band-blue) 100%);
  }
</style>
</head>
<body>
<main class="sheet">

  <section class="card card--front-a" aria-label="Card front">
    <div class="front-mark"><span class="mark-dot"></span><span class="mark-name">LORM</span></div>
  </section>

  <section class="card card--back-a" aria-label="Card back, blue edition">
    <div class="holder">
      <p class="holder-name">Daniel Corvey</p>
      <p class="holder-title holder-title--blue">President</p>
    </div>
    <div class="back-mark"><span class="mark-dot"></span><span class="mark-name">LORM</span></div>
    <p class="detail address">Address 220 Harbor Lane<span class="indent">Westbridge, Oregon 97410</span></p>
    <p class="detail personal">Phone # 5552104837<br>Cell # 5553182964<br>Email Id: info@lormmail.net</p>
    <p class="detail company-line">Co Phone # 5552104837<span class="gap"></span>Co Fax # 5557421093<br>Co Website: www.lormweb.net</p>
  </section>

  <section class="card card--front-b" aria-label="Card front">
    <div class="front-mark"><span class="mark-dot"></span><span class="mark-name">LORM</span></div>
  </section>

  <section class="card card--back-b" aria-label="Card back, colour band edition">
    <div class="holder">
      <p class="holder-name">Daniel Corvey</p>
      <p class="holder-title holder-title--red">President</p>
    </div>
    <p class="detail address">Address 220 Harbor Lane<span class="indent">Westbridge, Oregon 97410</span></p>
    <p class="detail personal">Phone # 5552104837<br>Cell # 5553182964<br>Email Id: info@lormmail.net</p>
    <p class="detail company-col">Co Phone # 5552104837<br>Co Fax # 5557421093<br>Co Website: www.lormweb.net</p>
    <div class="color-band" role="img" aria-label="Decorative green, yellow and blue colour band along the card's lower edge"></div>
  </section>

</main>
</body>
</html>
```